Business Card Design

We need a business card design for an existing business. Our main trading brand is www.brightquillsaver.co.uk

We attach various logo files - please use the version that will produce the sharpest image on the business card.

We are flexible about shape of card etc. Please think outside the box as to what goes on front and what goes on back of the card

We want to be able to amend the card (once the design has been agreed ) to add additional staff details, but the text to go on it will be generic

Details to go on card ( for the first generic one) are fairly minimal as we don't like cluttered business cards:-

Neil Cathcart
Managing Director

Mobile: 07841 258 407
Email: n.cathcart@brightquillsaver.co.uk

Industry/Entity Type

Business

```html
<!DOCTYPE html>
<html lang="en">
<head>
<meta charset="utf-8">
<title>Bright Quill Saver – Business Card</title>
<link rel="stylesheet" href="https://fonts.googleapis.com/css2?family=Lato:wght@400;700&display=swap">
<style>
  :root {
    --backdrop: #e9e6e2;
    --card-black: #0c0c0d;
    --card-sheen: #1b1b1d;
    --accent-blue: #4fa9d9;
    --text-light: #e8e8e8;
    --mark-faint: #3b3532;
  }
  * { box-sizing: border-box; margin: 0; padding: 0; }
  html, body {
    width: 1200px;
    height: 1023px;
    overflow: hidden;
    background: var(--backdrop);
    font-family: "Lato", Arial, sans-serif;
  }
  .stage {
    width: 1200px;
    height: 1023px;
    display: flex;
    flex-direction: column;
    align-items: center;
    justify-content: center;
    gap: 64px;
  }
  .card {
    position: relative;
    width: 620px;
    height: 396px;
    border-radius: 30px;
    background: linear-gradient(160deg, var(--card-sheen) 0%, var(--card-black) 45%, var(--card-black) 100%);
    overflow: hidden;
  }

  /* Front */
  .front-website {
    position: absolute;
    top: 34px;
    right: 40px;
    font-size: 21px;
    color: var(--text-light);
    letter-spacing: 0.2px;
  }
  .front-website .domain { color: var(--accent-blue); }
  .front-brand {
    position: absolute;
    left: 44px;
    bottom: 60px;
    display: flex;
    align-items: center;
    gap: 22px;
    font-size: 58px;
    font-weight: 700;
    color: var(--mark-faint);
  }
  .front-brand .dot {
    width: 64px;
    height: 64px;
    border-radius: 50%;
    background: var(--mark-faint);
  }

  /* Back */
  .contact-block {
    position: absolute;
    top: 40px;
    left: 44px;
    color: var(--text-light);
  }
  .person-name {
    font-size: 27px;
    font-weight: 700;
    color: var(--accent-blue);
  }
  .person-role {
    font-size: 19px;
    margin-top: 4px;
  }
  .contact-list {
    list-style: none;
    margin-top: 22px;
    font-size: 19px;
    line-height: 30px;
  }
  .contact-list li {
    display: flex;
    align-items: center;
    gap: 12px;
  }
  .contact-list svg {
    width: 18px;
    height: 18px;
    flex: none;
  }
  .back-brand {
    position: absolute;
    right: 44px;
    bottom: 44px;
    display: flex;
    align-items: center;
    gap: 12px;
    font-size: 26px;
    font-weight: 700;
    color: var(--accent-blue);
  }
  .back-brand .dot {
    width: 22px;
    height: 22px;
    border-radius: 50%;
    background: var(--accent-blue);
  }
</style>
</head>
<body>
<main class="stage">
  <section class="card card-front" aria-label="Card front">
    <p class="front-website">www.<span class="domain">brightquillsaver</span>.co.uk</p>
    <div class="front-brand"><span class="dot"></span>brightquillsaver</div>
  </section>

  <section class="card card-back" aria-label="Card back">
    <div class="contact-block">
      <h1 class="person-name">Neil Cathcart</h1>
      <p class="person-role">Managing Director</p>
      <ul class="contact-list">
        <li>
          <svg viewBox="0 0 18 18" aria-hidden="true"><rect x="4.5" y="1.5" width="9" height="15" rx="1.5" fill="none" stroke="#e8e8e8" stroke-width="1.5"/></svg>
          07841 258 407
        </li>
        <li>
          <svg viewBox="0 0 18 18" aria-hidden="true"><rect x="1.5" y="3.5" width="15" height="11" fill="#e8e8e8"/><path d="M1.5 3.5 L9 10 L16.5 3.5" fill="none" stroke="#0c0c0d" stroke-width="1.4"/></svg>
          n.cathcart@brightquillsaver.co.uk
        </li>
        <li>
          <svg viewBox="0 0 18 18" aria-hidden="true"><circle cx="9" cy="9" r="7.5" fill="none" stroke="#e8e8e8" stroke-width="1.4"/><ellipse cx="9" cy="9" rx="3.2" ry="7.5" fill="none" stroke="#e8e8e8" stroke-width="1.2"/><path d="M1.5 9 H16.5 M3 5 H15 M3 13 H15" stroke="#e8e8e8" stroke-width="1.1"/></svg>
          www.brightquillsaver.co.uk
        </li>
      </ul>
    </div>
    <div class="back-brand"><span class="dot"></span>brightquillsaver</div>
  </section>
</main>
</body>
</html>
```